Harbor Dental New Patient Ad designed to catch a persons eye in a busy and cluttered newspaper

a minimalist newspaper ad to attract new patients to my office. i want an ad that is reminiscent of the Look Further Quince ads of 1998 or the 1960 Faltmobil "Turnip" ad. I would like the words Simply Bright in the middle of a blank space with the logo above, and the website and phone number with $88 new patient special info below it. The address need not be on the ad just that it is in North Haven.
i am trying to convey a modern office that does quality work with a vivid, colorful minimalist ad that catches the eye with its style and simplicity. Comparative ads in my area are very busy, generic, and homogenous.

Target Market(s)

Educated baby boomers
Health Conscious Millennials
Health Conscious Gen X

Font styles to use
Serif
Sans Serif

Colors
2369af
0493ce
00a990
abd037
fbed22
ffc214
f78f20

Requirements
Must have
• our logo
• our website
• our phone number
• $88 exam and cleaning
Nice to have
• a one word ad with one phrase in bold in the middle of blank space
• "Simply Bright"

```html
<!DOCTYPE html>
<html lang="en">
<head>
<meta charset="utf-8">
<title>Harbor Dental – Simply Bright</title>
<link href="https://fonts.googleapis.com/css2?family=Open+Sans:ital,wght@0,400;0,700;1,600;1,700&display=swap" rel="stylesheet">
<style>
  :root {
    --brand-blue: #2369af;
    --bright-blue: #0493ce;
    --teal: #00a990;
    --lime: #abd037;
    --white: #ffffff;
    --backdrop: #e9e9e9;
  }
  * { margin: 0; padding: 0; box-sizing: border-box; }
  html, body {
    width: 1200px;
    height: 936px;
    overflow: hidden;
    background: var(--backdrop);
    font-family: "Open Sans", Arial, sans-serif;
  }
  .ad {
    position: absolute;
    left: 289px;
    top: 28px;
    width: 622px;
    height: 880px;
    background: radial-gradient(circle at 50% 24%, var(--bright-blue) 0%, #1a7dc0 22%, var(--brand-blue) 46%, var(--brand-blue) 100%);
    box-shadow: 0 18px 40px rgba(0,0,0,0.22);
    overflow: hidden;
  }
  .brand-name {
    position: absolute;
    top: 146px;
    left: 0;
    width: 100%;
    text-align: center;
    font-weight: 700;
    font-size: 22px;
    line-height: 1;
    color: var(--lime);
  }
  .headline {
    position: absolute;
    left: 170px;
    top: 352px;
    font-style: italic;
    line-height: 1;
    letter-spacing: -3px;
  }
  .headline-soft {
    display: block;
    font-weight: 600;
    font-size: 80px;
    color: var(--white);
  }
  .headline-bold {
    display: block;
    margin-left: 16px;
    margin-top: -14px;
    font-weight: 700;
    font-size: 98px;
    color: var(--lime);
  }
  .offer {
    position: absolute;
    left: 65px;
    top: 814px;
    font-weight: 700;
    font-size: 12.5px;
    letter-spacing: 1.6px;
    color: var(--teal);
    line-height: 17px;
  }
  .contact-bar {
    position: absolute;
    left: 257px;
    right: 0;
    top: 814px;
    height: 17px;
    background: var(--teal);
    color: var(--white);
    font-size: 9.5px;
    line-height: 17px;
    padding-left: 31px;
  }
  .contact-bar .divider { margin: 0 6px; }
</style>
</head>
<body>
  <main class="ad">
    <header class="brand-name">Harbor Dental</header>

    <h1 class="headline">
      <span class="headline-soft">Simply</span>
      <span class="headline-bold">Bright</span>
    </h1>

    <p class="offer">$88 EXAM &amp; CLEANING</p>
    <p class="contact-bar">203-555-0148<span class="divider">|</span>www.harbordental-nh.com</p>
  </main>
</body>
</html>
```